HOME IMPROVEMENT Business Card

I want a very unique business card. nothing typical and boring. Im open to you ideas. Ive seen cards with gold and silver or color foil and spot UV coatings. Im looking for something that looks cool and grabs attention. I like rounded corners but am open to all suggestions. We are a home improvement company and I will have a presentation folder printed and a catalog printed also and want to keep that same theme. I love the colors in our logo but I am open at looking at a 3rd color that would work with my logo. I hope that helps.
Card should include
Address
Phone
Fax
Email
Website
Target Market(s)
Home owners, people looking to remodel their home
Industry/Entity Type
Home Improvement
Contact Information for Business Card
2873 Maple Crest Avenue Unit 410
Linden Park, Il 60284
Phone
Direct Line
Email
Website
Font styles to use
Other font styles liked:
- IM OPEN MINDED
Requirements
Must have
- High end quality look nothing boring I like rounded corners but am open minded
Nice to have
- WOW. I want something nice and impressive.
Should not have
- ??? Not sure

```html
<!DOCTYPE html>
<html lang="en">
<head>
<meta charset="utf-8">
<title>Nestline Remodeling – Business Card</title>
<link href="https://fonts.googleapis.com/css2?family=Open+Sans:wght@400;600;700;800&display=swap" rel="stylesheet">
<style>
  :root {
    --green: #0a9a3a;
    --navy: #141c3c;
    --white: #ffffff;
    --ink: #3a3a3a;
    --backdrop: #d9dbde;
    --rule: #cfcfcf;
  }
  * { margin: 0; padding: 0; box-sizing: border-box; }
  html, body { width: 1200px; height: 977px; overflow: hidden; }
  body {
    background: var(--backdrop);
    font-family: "Open Sans", sans-serif;
    position: relative;
  }
  .card {
    position: absolute;
    left: 250px;
    width: 700px;
    height: 400px;
    border-radius: 14px;
    overflow: hidden;
    box-shadow: 0 6px 18px rgba(0,0,0,0.18);
  }
  .card-front { top: 59px; background: var(--green); }
  .card-back { top: 518px; background: var(--white); }

  .brand {
    position: absolute;
    display: flex;
    align-items: center;
    gap: 12px;
    font-weight: 800;
    letter-spacing: 0.5px;
  }
  .brand-mark { width: 22px; height: 22px; }
  .card-front .brand {
    left: 0; right: 0; top: 0; bottom: 0;
    justify-content: center;
    color: var(--white);
    font-size: 50px;
  }
  .card-front .brand-mark { background: var(--white); }
  .card-back .brand {
    left: 60px; top: 170px;
    color: var(--navy);
    font-size: 40px;
  }
  .card-back .brand-mark { background: var(--navy); width: 18px; height: 18px; }

  .divider {
    position: absolute;
    left: 400px; top: 40px;
    width: 1px; height: 245px;
    background: linear-gradient(to bottom, rgba(0,0,0,0), var(--rule) 25%, var(--rule) 75%, rgba(0,0,0,0));
  }
  .contact {
    position: absolute;
    left: 430px; top: 48px;
    color: var(--ink);
    font-size: 13px;
    line-height: 1.45;
  }
  .contact-name { color: var(--green); font-size: 22px; font-weight: 400; line-height: 1.1; }
  .contact-role { font-size: 13px; font-weight: 600; color: #222; margin-bottom: 10px; }
  .contact-address { margin-left: 22px; margin-bottom: 8px; }
  .contact-list { list-style: none; }
  .contact-list li { display: flex; align-items: center; gap: 14px; height: 23px; }
  .contact-list svg { width: 14px; height: 14px; fill: var(--green); flex: none; }

  .footer-bands { position: absolute; left: 0; bottom: 0; width: 700px; height: 90px; }
  .website {
    position: absolute;
    right: 40px; bottom: 38px;
    color: var(--white);
    font-size: 14px;
  }
</style>
</head>
<body>
  <section class="card card-front" aria-label="Card front">
    <div class="brand"><span class="brand-mark"></span>Nestline Remodeling</div>
  </section>

  <section class="card card-back" aria-label="Card back">
    <div class="brand"><span class="brand-mark"></span>Nestline</div>
    <div class="divider"></div>
    <div class="contact">
      <p class="contact-name">Daniel Reyes</p>
      <p class="contact-role">Manager</p>
      <p class="contact-address">2873 Maple Crest Avenue Unit 410<br>Linden Park, Il 60284</p>
      <ul class="contact-list">
        <li><svg viewBox="0 0 24 24"><path d="M6.6 10.8a15 15 0 0 0 6.6 6.6l2.2-2.2c.3-.3.7-.4 1-.2 1.1.4 2.3.6 3.6.6.6 0 1 .4 1 1V20c0 .6-.4 1-1 1A17 17 0 0 1 3 4c0-.6.4-1 1-1h3.5c.6 0 1 .4 1 1 0 1.3.2 2.5.6 3.6.1.3 0 .7-.2 1z"/></svg>847 555 0192</li>
        <li><svg viewBox="0 0 24 24"><path d="M7 1h10a2 2 0 0 1 2 2v18a2 2 0 0 1-2 2H7a2 2 0 0 1-2-2V3a2 2 0 0 1 2-2zm0 3v14h10V4zm5 15.5a1 1 0 1 0 0 2 1 1 0 0 0 0-2z"/></svg>847 555 0147</li>
        <li><svg viewBox="0 0 24 24"><path d="M7 2h8l3 3v4H7zM4 10h16a2 2 0 0 1 2 2v7H2v-7a2 2 0 0 1 2-2zm3 4v2h10v-2z"/></svg>847 555 0163</li>
        <li><svg viewBox="0 0 24 24"><path d="M2 5h20v2l-10 6L2 7zm0 4.3 10 6 10-6V19H2z"/></svg>info@nestlinebuild.com</li>
      </ul>
    </div>
    <svg class="footer-bands" viewBox="0 0 700 90" preserveAspectRatio="none" aria-hidden="true">
      <path d="M0 80 L700 62 L700 90 L0 90 Z" fill="var(--navy)"/>
      <path d="M430 66 Q440 30 470 28 L700 26 L700 62 Z" fill="var(--green)"/>
    </svg>
    <span class="website">www.nestlinebuild.com</span>
  </section>
</body>
</html>
```